Flyer für ambulanten Pflegedienst
Zielgruppe
Ambulanter Pflegedienst, Potentielle Kunden für Grund- und Behandlungspflege, nicht nur Pflegebedürftige, sondern auch Angehörige. Flyer dient zur Auslage, beispielsweise in Wartezimmern von Ärzten.
Aufgabenstellung
Ausführliches Briefing mit Aufbau und Text in der Anlage, ebenso das Bildmaterial, Fonts, Logos. Flyer in A4 Wickelfalz, bitte die Gestaltungsvorlage mit den Maßen des Druckanbieters (ebenfalls anbei) beachten. Vorerst hauptsächlich KI-generierte/Stockfotos vorhanden, Fotoshooting folgt im Juli und Bilder werden dann ggf. nochmal ersetzt um persönliche Ebene zu erzeugen. Der erste Wurf muss aber vorerst so erfolgen. Übergabe der Daten: Druckfähiges PDF, PDF mit Ebenen und AI

```html
<!DOCTYPE html>
<html lang="de">
<head>
<meta charset="utf-8">
<title>Flyer ambulanter Pflegedienst</title>
<link href="https://fonts.googleapis.com/css2?family=Outfit:wght@300;400;500;600;700;800&display=swap" rel="stylesheet">
<style>
:root{
  --blue:#1b3f9c;
  --blue-dark:#12307f;
  --ink:#111418;
  --grey:#5d6470;
  --panel:#eef2f8;
  --white:#ffffff;
  --green:#2f9a47;
  --line:#d6dce6;
}
*{margin:0;padding:0;box-sizing:border-box}
html,body{width:891px;height:1200px;overflow:hidden;background:#fff}
body{font-family:"Outfit",sans-serif;color:var(--ink);position:relative}
.panel{position:absolute;width:277px;height:581px;background:var(--panel);overflow:hidden}
.p1{left:17px;top:15px}.p2{left:308px;top:15px}.p3{left:599px;top:15px}
.p4{left:17px;top:609px}.p5{left:308px;top:609px}.p6{left:599px;top:609px}
.abs{position:absolute}
.photo{position:absolute}
.h1{font-weight:800;letter-spacing:-1px;line-height:.98;text-transform:uppercase}
.blue{color:var(--blue)}
.green{color:var(--green)}
.brand{display:flex;align-items:center;gap:4px;font-weight:600;color:var(--blue);font-size:10px}
.brand .dot{width:8px;height:8px;border-radius:50%;background:var(--blue)}
.tag{background:var(--blue);color:#fff;font-weight:700;font-size:8px;letter-spacing:.6px;padding:5px 7px}
.lead{font-size:7.4px;line-height:1.5;color:var(--ink)}
.check{position:absolute;left:30px;width:216px;height:24px;background:#fff;display:flex;align-items:center;gap:6px;padding-left:7px;font-size:8.4px;font-weight:600}
.check svg{width:8px;height:8px}
.body{font-size:7.2px;line-height:1.55;color:var(--ink)}
.small{font-size:6.8px;line-height:1.5;color:var(--grey)}
.service{position:absolute;left:22px;width:232px;display:flex;gap:10px}
.icon{flex:none;width:33px;height:33px;border-radius:50%;background:#fff;display:flex;align-items:center;justify-content:center}
.icon svg{width:16px;height:16px;fill:none;stroke:#3a3f48;stroke-width:1.3}
.service h3{font-size:9.6px;font-weight:500;margin:2px 0 3px}
.divider{position:absolute;left:22px;width:232px;height:1px;background:var(--line)}
.dots{position:absolute;left:26px;width:214px;border-top:1.5px dotted #c8ccd4}
.contact{display:flex;gap:5px;align-items:flex-start;font-size:7px;line-height:1.35;margin-bottom:3px}
.contact svg{flex:none;width:7px;height:7px;margin-top:1px;fill:currentColor}
</style>
</head>
<body>

<!-- Panel 1: Titel -->
<section class="panel p1">
  <div class="brand abs" style="left:30px;top:22px"><span class="dot"></span>brenner pflege</div>
  <div class="photo" role="img" aria-label="Foto: Pflegerin misst einer älteren Dame im Wohnzimmer den Blutdruck" style="left:62px;top:0;width:240px;height:260px;border-radius:130px 0 0 110px;background:linear-gradient(135deg,#d8c5ae,#a9b7c9 60%,#6f8fbf)"></div>
  <div class="photo" role="img" aria-label="Foto: lächelnde Pflegekraft im Gespräch mit einer Seniorin" style="left:62px;top:178px;width:124px;height:124px;border-radius:50%;border:4px solid #fff;background:linear-gradient(135deg,#e6d2bd,#8fa6cf)"></div>
  <div class="h1 abs" style="left:30px;top:318px;font-size:24px">Weil das eigene<br><span class="blue">Zuhause</span><br>Lebensqualität ist.</div>
  <div class="tag abs" style="left:30px;top:402px">IHR AMBULANTER PFLEGEDIENST FÜR DIE REGION.</div>
  <div class="abs lead" style="left:30px;top:431px;width:214px;border-left:1.5px solid var(--blue);padding-left:7px">For over 30 years, we have been supporting people in the Talheim and Bergau region in their own homes — individually, compassionately, and professionally.</div>
  <div class="check" style="top:476px"><svg viewBox="0 0 10 10"><circle cx="5" cy="5" r="5" fill="#1b3f9c"/><path d="M2.8 5.1l1.5 1.5 3-3" stroke="#fff" stroke-width="1.3" fill="none"/></svg>24h erreichbar</div>
  <div class="check" style="top:505px"><svg viewBox="0 0 10 10"><circle cx="5" cy="5" r="5" fill="#1b3f9c"/><path d="M2.8 5.1l1.5 1.5 3-3" stroke="#fff" stroke-width="1.3" fill="none"/></svg>Persönliche Beratung</div>
  <div class="check" style="top:534px"><svg viewBox="0 0 10 10"><circle cx="5" cy="5" r="5" fill="#1b3f9c"/><path d="M2.8 5.1l1.5 1.5 3-3" stroke="#fff" stroke-width="1.3" fill="none"/></svg>MD-geprüfte Qualität</div>
</section>

<!-- Panel 2: Wer wir sind -->
<section class="panel p2">
  <svg class="abs" style="left:0;top:0" width="277" height="250" viewBox="0 0 277 250">
    <path d="M125 30 L155 0 L180 0 L150 30Z" fill="#1b3f9c"/>
    <path d="M128 205 C160 245 230 240 277 200 L277 210 C230 252 160 255 122 215Z" fill="#1b3f9c"/>
  </svg>
  <div class="photo" role="img" aria-label="Foto: drei Pflegekräfte in blauer Dienstkleidung am Dienstwagen auf einer Wiese" style="left:30px;top:30px;width:216px;height:178px;border-radius:14px;background:linear-gradient(180deg,#bfd3ee 0%,#dfe7f1 45%,#8c8a6a 75%,#6d6a52)"></div>
  <div class="abs" style="left:30px;top:226px;background:var(--blue);color:#fff;font-size:8px;font-weight:600;padding:4px 14px;border-radius:10px">Wer wir sind</div>
  <div class="h1 abs" style="left:30px;top:254px;font-size:23.5px">Vertrauen <span class="blue">beginnt</span><br>mit Zuhören</div>
  <div class="abs body" style="left:30px;top:312px;width:206px">
    <p>Pflege bedeutet für uns mehr als Versorgung. Es geht um Menschen, ihre Gewohnheiten, ihre Wünsche und das gute Gefühl, in den eigenen vier Wänden bleiben zu können.</p>
    <p style="margin-top:9px">Deshalb nehmen wir uns Zeit für persönliche Gespräche und individuelle Lösungen. Gemeinsam mit unseren Kundinnen, Kunden und Angehörigen gestalten wir eine Unterstützung, die zum Leben passt – nicht umgekehrt.</p>
    <p style="margin-top:9px">Als ambulanter Pflegedienst begleiten wir Menschen im Raum Talheim und Bergau zuverlässig im Alltag und stehen auch Angehörigen beratend zur Seite.</p>
  </div>
  <div class="abs" style="left:30px;top:477px;width:216px;height:84px;border:1.3px solid var(--blue);border-radius:40px;display:flex;align-items:center;justify-content:center;text-align:center;font-size:10.4px;font-weight:500;line-height:1.35;padding:14px 18px 0">Unsere Pflege orientiert sich am Befinden der Menschen – nicht am Befund.“</div>
  <div class="abs" style="left:114px;top:458px;width:48px;height:36px;background:var(--panel)"></div>
  <svg class="abs" style="left:114px;top:458px" width="48" height="36" viewBox="0 0 48 36"><ellipse cx="24" cy="18" rx="22" ry="15" fill="none" stroke="#1b3f9c" stroke-width="2.5"/><text x="24" y="25" text-anchor="middle" font-family="Outfit" font-weight="800" font-size="20" fill="#1b3f9c">“</text></svg>
</section>

<!-- Panel 3: Leistungen -->
<section class="panel p3">
  <div class="abs blue" style="left:26px;top:36px;font-size:15px;font-weight:400">Unsere Leistungen</div>
  <div class="h1 abs" style="left:26px;top:64px;font-size:24px">Unterstützung,<br><span class="blue">die den Alltag</span><br>leichter <span class="blue">macht.</span></div>
  <div class="service" style="top:163px"><div class="icon"><svg viewBox="0 0 16 16"><path d="M8 11 4 7a2 2 0 0 1 4-2 2 2 0 0 1 4 2z"/><path d="M2 12h5l4 2 3-2"/></svg></div><div><h3>Grundpflege</h3><p class="small">Unterstützung bei Körperpflege, Mobilität, Ernährung und allem, was Sicherheit im Alltag gibt.</p></div></div>
  <div class="divider" style="top:214px"></div>
  <div class="service" style="top:232px"><div class="icon"><svg viewBox="0 0 16 16"><rect x="3" y="3" width="10" height="8" rx="1"/><path d="M8 5v4M6 7h4M2 13h5l4 1 3-2"/></svg></div><div><h3>Behandlungspflege</h3><p class="small">Medizinische Versorgung nach ärztlicher Verordnung – zum Beispiel Wundversorgung, Medikamentengabe oder Injektionen.</p></div></div>
  <div class="divider" style="top:290px"></div>
  <div class="service" style="top:304px"><div class="icon"><svg viewBox="0 0 16 16"><circle cx="9" cy="4" r="2"/><path d="M5 10a4 4 0 0 1 8 0M2 13h5l4 1 3-2"/></svg></div><div><h3>Betreuung &amp; Alltagsbegleitung</h3><p class="small">Begleitung im Alltag, stundenweise Betreuung, Unterstützung bei Demenz sowie Entlastung für Angehörige.</p></div></div>
  <div class="divider" style="top:363px"></div>
  <div class="service" style="top:377px"><div class="icon"><svg viewBox="0 0 16 16"><circle cx="8" cy="4" r="2"/><path d="M4 13a4 4 0 0 1 8 0M2 9l2 1M14 9l-2 1"/></svg></div><div><h3>Verhinderungspflege</h3><p class="small">Auszeiten im Rahmen der Verhinderungspflege, denn auch pflegende Angehörige müssen mal durchatmen.</p></div></div>
  <div class="divider" style="top:429px"></div>
  <div class="service" style="top:443px"><div class="icon"><svg viewBox="0 0 16 16"><rect x="2" y="2" width="5" height="3"/><rect x="9" y="2" width="5" height="3"/><circle cx="5" cy="9" r="1.5"/><circle cx="11" cy="9" r="1.5"/><path d="M3 14v-2h4v2M9 14v-2h4v2"/></svg></div><div><h3>Beratung</h3><p class="small">Pflegeberatung nach § 37.3 SGB XI zur Sicherstellung des Pflegegeld-Bezugs, Unterstützung bei Anträgen und Hilfe bei allen Fragen rund um Pflegeleistungen.</p></div></div>
  <svg class="abs" style="left:0;top:470px" width="277" height="111" viewBox="0 0 277 111"><path d="M0 75 C80 70 200 60 277 0 L277 111 L0 111Z" fill="#1b3f9c"/></svg>
</section>

<!-- Panel 4: Weitere Leistungen -->
<section class="panel p4">
  <div class="h1 abs blue" style="left:25px;top:31px;font-size:24px">Unsere<br>Leistungen</div>
  <div class="service" style="left:17px;top:100px"><div class="icon"><svg viewBox="0 0 16 16"><path d="M3 7 8 3l5 4v6H3z"/><path d="M8 7v4M6 9h4"/></svg></div><div><h3>Hausnotruf &amp; Erreichbarkeit</h3><p class="small">Sicherheit rund um die Uhr – mit einem Team, das erreichbar bleibt.</p></div></div>
  <div class="divider" style="left:17px;width:248px;top:150px"></div>
  <div class="service" style="left:17px;top:163px"><div class="icon"><svg viewBox="0 0 16 16"><rect x="3" y="2" width="9" height="12" rx="1"/><path d="M5 5h5M5 8h3M9 11l2 2 3-3"/></svg></div><div><h3>Palliative Versorgung</h3><p class="small">Als spezialisierter Anbieter ist uns die Versorgung und Begleitung zum Ende des Lebens ein besonderes Herzensanliegen.</p></div></div>
  <svg class="abs" style="left:25px;top:224px" width="230" height="70" viewBox="0 0 230 70"><text x="0" y="18" font-family="Outfit" font-weight="800" font-size="20" fill="#1b3f9c">”</text><path d="M20 4v8M20 8H200a10 10 0 0 1 10 10V70" fill="none" stroke="#1b3f9c" stroke-width="2"/></svg>
  <div class="abs blue" style="left:27px;top:247px;font-size:12.6px;font-weight:500;line-height:1.22;width:190px">Unsere Pflege orientiert sich am Befinden der Menschen – nicht am Befund.”</div>
  <div class="photo" role="img" aria-label="Foto: Pfleger legt einer lachenden Seniorin eine Strickjacke um" style="left:0;top:328px;width:180px;height:253px;border-radius:0 120px 0 0;background:linear-gradient(160deg,#d9d3c6,#8ea3c9 55%,#c8c2b8)"></div>
  <div class="photo" role="img" aria-label="Foto: Pflegerin unterhält sich mit einer älteren Frau auf dem Sofa" style="left:135px;top:296px;width:160px;height:165px;border-radius:50%;background:linear-gradient(135deg,#cfd8c4,#7fa0cf 50%,#e6dccd)"></div>
  <svg class="abs" style="left:0;top:480px" width="277" height="101" viewBox="0 0 277 101"><path d="M0 68 C110 70 200 50 277 0 L277 101 L0 101Z" fill="#1b3f9c"/></svg>
</section>

<!-- Panel 5: Besonderheiten & Kontakt -->
<section class="panel p5">
  <div class="h1 abs" style="left:26px;top:32px;font-size:24px">Was uns<br><span class="blue">besonders</span> macht.</div>
  <div class="abs" style="left:26px;top:96px;font-size:14px;font-weight:400;line-height:1.1;width:220px">Gute Pflege entsteht durch Aufmerksamkeit, Erfahrung und ein verlässliches Team.</div>
  <div class="abs small" style="left:26px;top:150px;width:216px;font-size:6.9px;line-height:1.65">Bei der Hauskrankenpflege Brenner arbeiten engagierte Pflegekräfte, Betreuungskräfte und Fachpersonen Hand in Hand – mit Herz, Respekt und fachlicher Kompetenz. Über 40 Mitarbeitende geben Tag für Tag ihr Bestes für Sie und Ihre Angehörigen.</div>
  <div class="dots" style="top:203px"></div>
  <div class="abs" style="left:26px;top:214px;font-size:14px">Wir sind für Sie da.</div>
  <div class="abs small" style="left:26px;top:238px;width:216px;font-size:6.9px;line-height:1.65">Sie möchten sich informieren oder ein persönliches Gespräch vereinbaren? Wir beraten Sie gerne – unkompliziert, persönlich und unverbindlich.</div>
  <div class="dots" style="top:278px"></div>
  <div class="abs" style="left:26px;top:290px;font-size:11.6px;font-weight:600;line-height:1.25">Hauskrankenpflege Brenner Lindenweg 10 · 31000 Talheim</div>
  <div class="abs" style="left:26px;top:328px;width:220px">
    <div class="contact"><svg viewBox="0 0 10 10" style="color:#1b3f9c"><path d="M2 0l2 2-1 2 3 3 2-1 2 2-2 2C4 10 0 6 0 2z"/></svg>Telefon: 0 51 00 - 12 34 0</div>
    <div class="contact"><svg viewBox="0 0 10 10" style="color:#1b3f9c"><path d="M0 2h10v6H0zM0 2l5 3 5-3" /></svg>info@brenner-pflege.example</div>
    <div class="contact"><svg viewBox="0 0 10 10" style="color:#1b3f9c"><circle cx="5" cy="5" r="5"/></svg>www.brenner-pflege.example</div>
    <div class="contact"><svg viewBox="0 0 10 10" style="color:#1b3f9c"><path d="M5 0a3.5 3.5 0 0 1 3.5 3.5C8.5 6 5 10 5 10S1.5 6 1.5 3.5A3.5 3.5 0 0 1 5 0z"/></svg>Bürozeiten: Mo., Di., Mi., Fr. 9 bis 12 Uhr und Do. 15 bis 17 Uhr<br>Ergänzende Elemente</div>
  </div>
  <div class="photo" role="img" aria-label="Foto: Pflegekraft in blauer Jacke geht über eine Wiese zum Dienstwagen" style="left:0;top:400px;width:277px;height:181px;border-radius:60% 40% 0 0/20% 10% 0 0;background:linear-gradient(180deg,#c9d8ee,#e7ecf2 45%,#7c7a5e 70%,#5e5c48)"></div>
  <svg class="abs" style="left:0;top:388px" width="277" height="40" viewBox="0 0 277 40"><path d="M90 20 C150 -2 230 0 277 14 L277 22 C230 8 160 6 100 26Z" fill="#1b3f9c"/></svg>
  <div class="abs" style="left:18px;top:400px;width:84px;height:60px;border-radius:50%;background:#fff;display:flex;align-items:center;justify-content:center"><div class="brand" style="font-size:9px"><span class="dot"></span>brenner pflege</div></div>
</section>

<!-- Panel 6: Haushaltsdienst -->
<section class="panel p6">
  <div class="h1 abs" style="left:22px;top:33px;font-size:24px">Haushaltsdienst<br><span class="green">Leistungen</span></div>
  <div class="abs" style="left:22px;top:87px;font-size:11.4px;font-weight:500">Haushaltshilfe. Entlastung im Alltag.</div>
  <div class="abs small" style="left:22px;top:109px;width:236px;font-size:6.8px;line-height:1.65">Damit Sie sich weiterhin zu Hause wohlfühlen, bietet Ihnen das Team von Brenner Hausdienste mit über 25 Kolleginnen und Kollegen professionelle und zuverlässige Unterstützung in verschiedenen Bereichen:</div>
  <div class="service" style="top:156px"><div class="icon"><svg viewBox="0 0 16 16"><path d="M8 10 5 7a1.6 1.6 0 0 1 3-1.5A1.6 1.6 0 0 1 11 7z"/><circle cx="8" cy="7.5" r="5.5"/></svg></div><div><h3>Haushaltshilfe</h3><p class="small" style="line-height:1.3">Unterstützung bei alltäglichen Aufgaben – von der gründlichen Reinigung bis zur Wäsche.</p></div></div>
  <div class="divider" style="top:199px"></div>
  <div class="service" style="top:210px"><div class="icon"><svg viewBox="0 0 16 16"><path d="M8 14 2 8a3.5 3.5 0 0 1 6-4 3.5 3.5 0 0 1 6 4z"/></svg></div><div><h3>Begleitung</h3><p class="small" style="line-height:1.3">Niemand ist gern allein, und wir sind für Sie da, wenn Sie Gesellschaft wünschen</p></div></div>
  <div class="divider" style="top:251px"></div>
  <div class="service" style="top:261px"><div class="icon"><svg viewBox="0 0 16 16"><path d="M3 7 8 3l5 4v6H3z"/><path d="M8 7v4M6 9h4"/></svg></div><div><h3>Pflege</h3><p class="small" style="line-height:1.3">Strukturierte Pflege und Unterstützung, individuell auf Ihre Bedürfnisse abgestimmt.</p></div></div>
  <div class="abs" style="left:32px;top:312px;font-size:14.4px">So erreichen Sie uns</div>
  <div class="abs small" style="left:32px;top:336px;width:224px;font-size:6.9px;line-height:1.65">Das Team von Brenner Home Services hilft Ihnen gerne bei Fragen und Terminwünschen weiter.</div>
  <svg class="abs" style="left:0;top:425px" width="277" height="156" viewBox="0 0 277 156"><path d="M0 30 C60 0 140 -4 277 10 L277 156 L0 156Z" fill="#2f9a47"/><path d="M8 22 C70 -6 150 -8 260 4" fill="none" stroke="#2f9a47" stroke-width="3"/></svg>
  <div class="photo" role="img" aria-label="Foto: lächelnde Mitarbeiterin im grünen Oberteil" style="left:157px;top:389px;width:102px;height:102px;border-radius:50%;border:4px solid #fff;background:linear-gradient(160deg,#e8ddd2,#b9a48f 55%,#3f8e55)"></div>
  <div class="abs" style="left:26px;top:462px;color:#fff;font-size:12px;font-weight:700;line-height:1.15">Brenner Hausdienste<br>GmbH</div>
  <div class="abs" style="left:26px;top:497px;width:160px;color:#fff">
    <div class="contact"><svg viewBox="0 0 10 10"><path d="M2 0l2 2-1 2 3 3 2-1 2 2-2 2C4 10 0 6 0 2z"/></svg>Telefon: +49 51 00 - 98 76 543</div>
    <div class="contact"><svg viewBox="0 0 10 10"><path d="M0 2h10v6H0z"/></svg>info@brenner-hausdienste.example</div>
    <div class="contact"><svg viewBox="0 0 10 10"><circle cx="5" cy="5" r="5"/></svg>www.brenner-hausdienste.example</div>
    <div class="contact"><svg viewBox="0 0 10 10"><path d="M5 0a3.5 3.5 0 0 1 3.5 3.5C8.5 6 5 10 5 10S1.5 6 1.5 3.5A3.5 3.5 0 0 1 5 0z"/></svg>Bürozeiten: Mo., Di., Mi., Fr. 9 bis 12 Uhr und Do. 15 bis 17 Uhr Ergänzende Elemente</div>
  </div>
  <div class="abs" style="left:190px;top:548px;display:flex;align-items:center;gap:4px;color:#fff;font-size:10px;font-weight:600"><span style="width:8px;height:8px;border-radius:50%;background:#fff"></span>brenner dienste</div>
</section>

</body>
</html>
```